Online-Marketing Material für Bewegungsangebot speziell für Kinder
Zielgruppe
Hopsalino bietet ein hochwertiges, sportwissenschaftlich fundiertes Bewegungsangebot speziell für Kinder an. Unsere Kurse verbinden spielerische Elemente mit modernen Trainingsmethoden und schaffen eine liebevolle Umgebung in der Kinder ganz ohne Druck wachsen, lernen und sich mit Freude bewegen.
Unsere Zielgruppe sind Eltern mit Kindern zwischen zwei und acht Jahren, die ein qualitativ sehr hochwertiges Sportprogramm für ihre Kinder suchen und großen Wert auf professionelle Förderung, Sicherheit und eine warmherzige Atmosphäre legen.
Aufgabenstellung
Die Kreativen sollen berücksichtigen, dass der neue Hero ein echter Eye Catcher sein muss. Er soll sofort ein Wow-Gefühl auslösen und viel stärker auffallen als die aktuelle, eher schlichte Hero Section. Die Gestaltung soll hochwertig, kindlich liebevoll und gleichzeitig modern wirken. Der neue Hero muss sich perfekt in das bestehende Webdesign einfügen und die Hopsalino Welt auf den ersten Blick spürbar machen. Der bestehende Text bleibt zwingend erhalten. Alles andere darf kreativ neu gedacht werden, solange das Ergebnis direkt Aufmerksamkeit fängt, Emotionen weckt und die hohe Qualität des Sportangebots im Kindersegment sichtbar macht.
Ich benötige ein vollständiges Redesign ausschließlich für die Hero Section meiner Website www.hopsalino-kurse.example. Das restliche Webdesign passt bereits sehr gut zu meiner Marke, doch die aktuelle Hero Section wirkt noch zu schlicht und erzeugt kein echtes Wow-Gefühl.
Hopsalino steht für ein hochwertiges, sportwissenschaftlich fundiertes Sportangebot für Kinder zwischen zwei und acht Jahren. Unsere Welt ist liebevoll, warm, spielerisch und gleichzeitig sehr professionell. Genau dieses Gefühl soll der neue Hero sofort transportieren.
Wichtige Vorgaben
• Es geht ausschließlich um die Hero Section
• Der bestehende Text muss unbedingt erhalten bleiben
• Das Design soll hochwertig, kindlich, warm und liebevoll wirken
• Optisch nahtlose Anpassung an das bestehende Webdesign
• Der neue Hero soll ein klarer Eye Catcher sein und ein echtes Wow erzeugen
• Kreative Freiheit in der Gestaltung, solange alles modern, hochwertig und zur Hopsalino Welt passend bleibt
Mir ist wichtig, dass der neue Hero direkt Emotionen weckt und die hohe Qualität unseres Kinder-Sportangebots schon auf den ersten Blick spürbar macht.

```html
<!DOCTYPE html>
<html lang="en">
<head>
<meta charset="utf-8">
<title>Hopsalino – Ball School Hero</title>
<link href="https://fonts.googleapis.com/css2?family=Montserrat:wght@500;600;800;900&family=Lato:wght@400;700&display=swap" rel="stylesheet">
<style>
  :root {
    --white: #ffffff;
    --ink: #1c1c1c;
    --brand-blue: #2fa8df;
    --gold: #efd17c;
    --gold-ring: #b8923a;
    --hero-top: #e4e2e6;
    --hero-mid: #cfd0e0;
    --hero-low: #c9cbdc;
    --floor: #d5d5d7;
  }
  * { box-sizing: border-box; margin: 0; padding: 0; }
  html, body { width: 1200px; height: 1026px; overflow: hidden; background: var(--white); }
  body { position: relative; font-family: "Montserrat", sans-serif; color: var(--ink); }

  .site-header {
    position: absolute; left: 0; top: 0; width: 1200px; height: 158px;
    background: var(--white);
  }
  .brand {
    position: absolute; left: 43px; top: 58px;
    display: flex; align-items: center; gap: 8px;
    font-family: "Montserrat", sans-serif; font-weight: 800; font-size: 22px;
    color: var(--ink); letter-spacing: 0.2px;
  }
  .brand-dot {
    width: 14px; height: 14px; border-radius: 50%; background: var(--gold-ring);
  }
  .main-nav {
    position: absolute; left: 407px; top: 73px;
    display: flex; gap: 22px;
    font-size: 18px; font-weight: 500; letter-spacing: 0.4px;
  }
  .main-nav a { color: var(--ink); text-decoration: none; }
  .locations-btn {
    position: absolute; left: 995px; top: 64px; width: 153px; height: 37px;
    background: var(--gold); border-radius: 4px;
    display: flex; align-items: center; justify-content: center; gap: 7px;
    font-family: "Lato", sans-serif; font-size: 19px; color: var(--ink);
  }

  .hero {
    position: absolute; left: 0; top: 158px; width: 1200px; height: 868px;
    overflow: hidden;
  }
  .hero-backdrop {
    position: absolute; inset: 0;
    background: linear-gradient(180deg, var(--hero-top) 0%, var(--hero-mid) 35%, var(--hero-low) 70%, var(--floor) 100%);
  }
  .hero-title {
    position: absolute; left: 42px; top: 99px;
    font-weight: 900; font-size: 45px; line-height: 43px;
    color: var(--brand-blue); text-transform: uppercase; letter-spacing: 0.3px;
  }
  .hero-copy {
    position: absolute; left: 42px; top: 253px; width: 680px;
    font-weight: 500; font-size: 20.5px; line-height: 28.5px; color: var(--ink);
  }
  .cta {
    position: absolute; left: 41px; top: 428px; width: 369px; height: 53px;
    background: var(--brand-blue); border-radius: 5px;
    display: flex; align-items: center; justify-content: center;
    font-weight: 600; font-size: 21px; color: var(--white); letter-spacing: 0.3px;
  }
  .photo-card {
    position: absolute; background: var(--white); border-radius: 18px; padding: 7px;
    box-shadow: 0 4px 14px rgba(0,0,0,0.12);
  }
  .photo-card .photo { width: 100%; height: 100%; border-radius: 12px; }
  .card-header-kid { left: 924px; top: 167px; width: 228px; height: 333px; }
  .card-header-kid .photo { background: linear-gradient(180deg, #b8a994 0%, #4f9ae0 55%, #6a6a5c 100%); }
  .card-kick { left: 739px; top: 55px; width: 228px; height: 334px; }
  .card-kick .photo { background: linear-gradient(180deg, #8fa3b6 0%, #3d6a4c 45%, #2f8a4a 100%); }

  .carousel { position: absolute; left: 0; top: 0; width: 1200px; height: 1026px; }
</style>
</head>
<body>
  <header class="site-header">
    <div class="brand"><span class="brand-dot"></span>Hopsalino</div>
    <nav class="main-nav">
      <a href="#">CONCEPT</a>
      <a href="#">FRANCHISE</a>
      <a href="#">CONTACT</a>
    </nav>
    <div class="locations-btn">
      <svg width="12" height="18" viewBox="0 0 12 18" aria-hidden="true"><path d="M6 0a6 6 0 0 0-6 6c0 4.5 6 12 6 12s6-7.5 6-12a6 6 0 0 0-6-6z" fill="#e2405a"/><circle cx="6" cy="6" r="2.2" fill="#f7a3b1"/></svg>
      Locations
      <svg width="12" height="8" viewBox="0 0 12 8" aria-hidden="true"><path d="M1.5 1.5 6 6l4.5-4.5" fill="none" stroke="#1c1c1c" stroke-width="2"/></svg>
    </div>
  </header>

  <section class="hero">
    <div class="hero-backdrop" role="img" aria-label="Faded background photo of a group of children in blue shirts huddling together"></div>
    <h1 class="hero-title">Your ball school<br>for children aged<br>2 and up</h1>
    <p class="hero-copy">Dodge stink bombs, rescue your ball, and fly into space.<br>At Hopsalino, children don't just become little movement experts; we offer so much more. Motor skills, coordination, and targeted brain training playfully and holistically promote your child's development in a loving environment.</p>
    <a class="cta">FIND A COURSE NEAR YOU</a>

    <div class="photo-card card-header-kid"><div class="photo" role="img" aria-label="Boy in a blue kit balancing a football on his head"></div></div>
    <div class="photo-card card-kick"><div class="photo" role="img" aria-label="Boy in a blue shirt kicking a ball on an artificial pitch with palm trees"></div></div>
  </section>

  <svg class="carousel" viewBox="0 0 1400 1197" width="1200" height="1026">
    <defs>
      <linearGradient id="g-team" x1="0" y1="0" x2="0" y2="1"><stop offset="0" stop-color="#8fa07a"/><stop offset="1" stop-color="#3f6fb8"/></linearGradient>
      <linearGradient id="g-mascot" x1="0" y1="0" x2="1" y2="0"><stop offset="0" stop-color="#8b8b8b"/><stop offset="1" stop-color="#6a4a30"/></linearGradient>
      <linearGradient id="g-court" x1="0" y1="0" x2="0" y2="1"><stop offset="0" stop-color="#9aa0a8"/><stop offset="0.3" stop-color="#6f7680"/><stop offset="0.35" stop-color="#2e78c0"/><stop offset="1" stop-color="#2466a8"/></linearGradient>
      <linearGradient id="g-garden" x1="0" y1="0" x2="0" y2="1"><stop offset="0" stop-color="#5c7a45"/><stop offset="0.6" stop-color="#3d70c2"/><stop offset="1" stop-color="#d9e0d0"/></linearGradient>
      <linearGradient id="g-wall" x1="0" y1="0" x2="0" y2="1"><stop offset="0" stop-color="#8c8e90"/><stop offset="0.75" stop-color="#6e655c"/><stop offset="1" stop-color="#8a6a48"/></linearGradient>
    </defs>
    <g role="img" aria-label="Children in blue team shirts on grass">
      <polygon points="0,890 57,897 57,1125 0,1135" fill="url(#g-team)"/>
    </g>
    <g role="img" aria-label="Toddler hugging a brown bear mascot">
      <polygon points="64,860 300,885 300,1138 64,1165" fill="url(#g-mascot)"/>
    </g>
    <g role="img" aria-label="Blue outdoor sports court with cones and children playing">
      <polygon points="301,852 629,870 629,1155 301,1165" fill="url(#g-court)"/>
    </g>
    <g role="img" aria-label="Smiling little girl in a blue shirt in a garden">
      <polygon points="631,858 974,851 974,1165 631,1165" fill="url(#g-garden)"/>
    </g>
    <g role="img" aria-label="Coach with a child and the bear mascot indoors">
      <polygon points="975,870 1243,856 1243,1165 975,1165" fill="url(#g-wall)"/>
    </g>
    <g role="img" aria-label="Children running on a blue court under trees">
      <polygon points="1244,893 1385,874 1385,1150 1244,1130" fill="url(#g-court)"/>
    </g>
  </svg>
</body>
</html>
```